Pellow Ridge Estate Wine Label and Logo

We require a new logo and label for our wine label Pellow Ridge Estate. See brief below for details.

Pellow Ridge is wholly owned by Marrowgate Wines, an established heritage brand that has existed for 40 years. The Pellow Ridge brand is created to make wines at a very competitive price point.

The wine market in Australia is divided more than ever into established “heritage” brands carrying a price premium, and less expensive brands jostling at the lower price point. Traditionalists are sticking mostly with heritage brands.

In the market the independent producers seem to be following in the steps of the independent beer market, using colourful and inventive designs – breaking from tradition, New younger drinkers are looking to experiment, and not drink what their parents are drinking.

With the logo we have, and we’re not capturing anyone’s interest or imagination.
We want a brand and label that’s eye catching - this helps in the off premise (liquor store) market, while still emoting quality at a café/restaurant wine list.

There’s no history to rely on here, and no market presence, so we need to be eye catching, while still implying quality and craftsmanship.

Target Market(s)

We’re aiming for a retail price point of AUD 15 per bottle, often discounted lower...
Customers are less motivated by quality, more aware that wine prices are competitive and want a bargain.
We’re targeting younger buyers breaking from tradition, and seeking a bargain at the same time. New younger drinkers are looking to experiment, and not drink what their parents are drinking.
We’re keen to target occasional drinkers aged 25 plus, who like to go out and enjoy wine, want it to be great, but not stuffy.

Font styles to use
Serif
Sans Serif

Colors

Designer to choose colors to be used in the design.

Requirements
Must have
• Details in attached PDF Design Brief.
Nice to have
Should not have

```html
<!DOCTYPE html>
<html lang="en">
<head>
<meta charset="utf-8">
<title>Pellow Ridge Estate – Wine Label</title>
<link rel="stylesheet" href="https://fonts.googleapis.com/css2?family=Josefin+Sans:wght@300;400&display=swap">
<style>
  :root {
    --backdrop: #ececec;
    --label-black: #121212;
    --gold: #c9a14f;
    --gold-soft: #a88a4c;
  }
  html, body {
    margin: 0;
    padding: 0;
    width: 1200px;
    height: 960px;
    overflow: hidden;
    background: var(--backdrop);
  }
  .canvas {
    position: relative;
    width: 1200px;
    height: 960px;
    display: flex;
    align-items: center;
    justify-content: center;
  }
  .wine-label {
    position: relative;
    width: 520px;
    height: 840px;
    background: var(--label-black);
    font-family: "Josefin Sans", "Helvetica Neue", Arial, sans-serif;
    color: var(--gold);
    text-transform: uppercase;
    text-align: center;
  }
  .brand-name {
    position: absolute;
    top: 118px;
    left: 0;
    right: 0;
    margin: 0;
    font-weight: 400;
    font-size: 40px;
    letter-spacing: 0.28em;
    padding-left: 0.28em;
    line-height: 1;
  }
  .brand-descriptor {
    position: absolute;
    top: 172px;
    left: 0;
    right: 0;
    display: flex;
    align-items: center;
    justify-content: center;
    gap: 14px;
    font-weight: 400;
    font-size: 15px;
    letter-spacing: 0.6em;
    line-height: 1;
  }
  .brand-descriptor .rule {
    display: block;
    width: 22px;
    height: 1px;
    background: var(--gold);
  }
  .brand-descriptor .word {
    padding-left: 0.6em;
  }
  .region {
    position: absolute;
    top: 256px;
    left: 0;
    right: 0;
    margin: 0;
    font-weight: 300;
    font-size: 13px;
    letter-spacing: 0.35em;
    padding-left: 0.35em;
    color: var(--gold-soft);
  }
  .origin {
    position: absolute;
    bottom: 40px;
    left: 0;
    right: 0;
    margin: 0;
    font-weight: 300;
    font-size: 14px;
    letter-spacing: 0.3em;
    padding-left: 0.3em;
    color: var(--gold-soft);
  }
</style>
</head>
<body>
  <main class="canvas">
    <section class="wine-label" aria-label="Pellow Ridge Estate wine label">
      <h1 class="brand-name">Pellow Ridge</h1>
      <div class="brand-descriptor">
        <span class="rule"></span>
        <span class="word">Estate</span>
        <span class="rule"></span>
      </div>
      <p class="region">Coralwood Valley</p>
      <p class="origin">Wine of Australia</p>
    </section>
  </main>
</body>
</html>
```